A poster for Vale Chiropractic's up coming powerful health workshop/seminar

I need a poster developed for Dr. Prent's upcoming Total Shape Reset and Armor Plating your Wellness seminar/workshop. This workshop will teach attendants how to shed pounds and rapidly reduce their waist size. Learn why weight loss doesn't work 99.9% of the time so that you can be the successful .1%. It's time to expose the LIES and reveal the TRUTH about the REAL causes of HEART DISEASE, DIABETES, CANCER, CHRONIC FATIGUE, ARTHRITIS, FIBROMYALGIA, and how to REVERSE/PREVENT this from ever happening to you or your family. The Insider Secrets to building your body into a health fortress unbreachable by sickness and disease. Learn to live and fufill your GOD-GIVEN health potential. Eliminate high bloodpressure, high cholesterol, diabetes, fatigue, chronic pain
Ending the WAR on sickness and disease by launching an unstoppable health offensive that will pummel any enemy of life and health.

I'm not a designer by any means, but was thinking of possible WAR theme, cammo, etc....just a thought. Not a requirement by any means
Updates

Dr. Prent has taken a look at all the submissions and has requested a few changes.

1. He wants the new map that has been added to the brief with Marlow Ridge College as a title above the map

2. He wants a section that describes what the attendees will gain at the seminar in bullet format.  Example:  Title....It's not about what you lose

                                                   I'ts about what you gain....

>The No-Hype, No- Gimmick  secrets for fast effective Weight loss

>How the top 3 disease killers, heart disease, cancer, and diabetes are linked to diet

>Tools and strategies to make 2012 the best year ever

The Seminar will be held at Marlow Ridge College, Tuesday January 3rd @ 6:30pm Open to Public

Target Market(s)

Adults 30-65

Industry/Entity Type

Building

Requirements
Should not have
• ruyrtur

```html
<!DOCTYPE html>
<html lang="en">
<head>
<meta charset="utf-8">
<title>Dr. Prent's Total Shape Reset and Armor Plating your Wellness Seminar</title>
<link rel="stylesheet" href="https://fonts.googleapis.com/css2?family=Roboto:wght@300;700&family=Open+Sans:wght@400;700&family=Roboto+Condensed:wght@400;700&display=swap">
<style>
  :root {
    --paper: #ffffff;
    --ink: #2b2b2b;
    --body-ink: #3a3a3a;
    --orange: #e8702a;
    --olive: #6f8a32;
    --red: #d8262b;
    --bullet: #e8742f;
    --suit-dark: #1c1c1f;
    --suit-mid: #3a3a40;
    --map-green: #6f7f5a;
    --map-grey: #a7aba3;
  }
  * { margin: 0; padding: 0; box-sizing: border-box; }
  html, body { width: 800px; height: 1200px; overflow: hidden; background: var(--paper); }
  .poster { position: relative; width: 800px; height: 1200px; background: var(--paper); overflow: hidden; }

  .speaker-photo {
    position: absolute; left: 0; top: 0; width: 290px; height: 1200px;
    background: linear-gradient(180deg, #f4f4f4 0%, #e9e6e3 10%, var(--suit-mid) 22%, var(--suit-dark) 55%, var(--suit-dark) 100%);
  }

  .seminar-title {
    position: absolute; left: 310px; top: 222px; width: 470px;
    font-family: "Roboto", Arial, sans-serif; font-weight: 300;
    font-size: 54px; line-height: 62px; letter-spacing: -2px; color: var(--ink);
  }
  .seminar-title .line { display: block; white-space: nowrap; }
  .seminar-title .accent-orange { color: var(--orange); font-weight: 700; letter-spacing: -1.5px; }
  .seminar-title .accent-olive { color: var(--olive); font-weight: 700; letter-spacing: -1.5px; }

  .talking-points {
    position: absolute; left: 289px; top: 515px; width: 458px; list-style: none;
    font-family: "Open Sans", Arial, sans-serif; font-size: 14.6px; line-height: 20.5px; color: var(--body-ink);
  }
  .talking-points > li { position: relative; padding-left: 24px; margin-bottom: 17px; }
  .talking-points > li::before {
    content: ""; position: absolute; left: 0; top: 5px; width: 11px; height: 11px; background: var(--bullet);
  }
  .talking-points strong { font-weight: 700; }

  .gain-list { list-style: none; margin-top: 3px; }
  .gain-list li { position: relative; padding-left: 16px; margin-bottom: 2px; }
  .gain-list li::before {
    content: ""; position: absolute; left: 1px; top: 7px;
    border-left: 7px solid var(--bullet); border-top: 4px solid transparent; border-bottom: 4px solid transparent;
  }

  .venue-map-title {
    position: absolute; left: 570px; top: 932px;
    font-family: "Roboto Condensed", Arial, sans-serif; font-size: 13px; color: var(--ink);
  }
  .venue-map {
    position: absolute; left: 570px; top: 950px; width: 178px; height: 136px;
    background: linear-gradient(135deg, var(--map-grey) 0%, var(--map-green) 55%, #8e948a 100%);
  }

  .event-when {
    position: absolute; left: 313px; top: 1008px;
    font-family: "Roboto Condensed", Arial, sans-serif; color: var(--body-ink);
  }
  .event-when .day, .event-when .place { font-size: 19px; line-height: 24px; }
  .event-when .date { font-size: 27px; line-height: 34px; font-weight: 700; color: var(--red); }
  .event-when .date sup { font-size: 15px; }

  .rsvp {
    position: absolute; left: 313px; top: 1112px;
    font-family: "Roboto Condensed", Arial, sans-serif; font-size: 19px; line-height: 24px; color: var(--body-ink);
    white-space: nowrap;
  }
  .rsvp strong { font-weight: 700; }
</style>
</head>
<body>
<main class="poster">
  <div class="speaker-photo" role="img" aria-label="Photo of Dr. Prent standing, smiling, in a dark suit with a pink tie"></div>

  <h1 class="seminar-title">
    <span class="line">Dr. Prent's Total</span>
    <span class="line"><span class="accent-orange">Shape Reset</span> and</span>
    <span class="line">Armor Plating your</span>
    <span class="line accent-olive">Wellness Seminar</span>
  </h1>

  <ul class="talking-points">
    <li><strong>Dr. Evan Prent, D.C.</strong> is going to reveal how he has helped hundreds of patients achieve rapid weight loss and drastically reduce their waist size.</li>
    <li>Learn why weight loss almost always fails and how you can succeed with a <strong>No-Hype, No-Gimmick, No-Starving</strong> yourself, and actually eat as much as you want weight loss approach for real health and real results.</li>
    <li>It's time to expose the <strong>LIES</strong> and reveal the <strong>TRUTH</strong> about the REAL causes of <strong>HEART DISEASE, DIABETES, CANCER, CHRONIC FATIGUE, ARTHRITIS, FIBROMYALGIA,</strong> and how to not be the victim and fight back.</li>
    <li><strong>It's not about what you lose...it's about what you gain.</strong>
      <ul class="gain-list">
        <li>The No-Hype, No-Gimmick secrets for fast effective weight loss</li>
        <li>How the top 3 disease killers, heart disease, cancer, and diabetes are linked to diet</li>
        <li>Tools and strategies to make 2012 the best year ever</li>
      </ul>
    </li>
  </ul>

  <p class="venue-map-title">Marlow Ridge College</p>
  <div class="venue-map" role="img" aria-label="Aerial map of Marlow Ridge College with the auditorium marked"></div>

  <div class="event-when">
    <p class="day">On Tuesday</p>
    <p class="date">January 3<sup>rd</sup>, at 6:30</p>
    <p class="place">At Marlow Ridge College</p>
  </div>

  <p class="rsvp">Call : <strong>555-014-2290</strong> to RSVP. Limited to 150 seats.<br>First 50 to register recieve a <strong>FREE GIFT</strong></p>
</main>
</body>
</html>
```